Real Estate Brochure Design Project For Client Appreciation Program

We're a residential real estate team, offering a complimentary rental program (moving, household, and party supplies). I'd like a brochure we can use to give the details of the program to our clients. Our team name is the Bramwell Estate Circle. I'd like a design that uses our company colors of red, along with black and/or gray accents. The design should convey that we're offering an innovative program not offered by others, as a way to give back to our clients.

Target Market(s)

Our preferred clients. Home buyers and sellers, attorneys, property managers, other Realtors

Industry/Entity Type

Residential

Requirements
Must have
• The brochure must have photos of some of the items available for rent. (Popcorn Machine, Margarita Machine, Moving Van, Power Tools, etc) You can find some of these at www.tpvintagehire.ex. It should be a trifold brochure, yet does not need to have 3 separate panels on the inside. It must include our company logo which I've uploaded, as well as carry our corporate identity which can be seen at the following website, which is the template for our website re-design. http://danfolwick.plumvesta.ex/

I've included in the attachments, a brochure with text. I'd like the text highlighted in yellow to be incorporated. It must be editable for slight edits to be made.
I've also attached a photo of a man giving out cotton candy. These are the types of photos I'd love to be included.
I've also attached the photo which is the one from the website header mentioned above.

Lastly, I'd like an image of a typical real estate moving van, with our logo on the side, so it looks like a photo of our truck. I don't want our actual truck image, as it is more generic to just Tanner Pollard and not our team.

```html
<!DOCTYPE html>
<html lang="en">
<head>
<meta charset="utf-8">
<title>Bramwell Estate Circle – Client Appreciation Trifold</title>
<link href="https://fonts.googleapis.com/css2?family=Caladea:wght@400;700&display=swap" rel="stylesheet">
<style>
  :root{
    --red:#e0242b;
    --red-deep:#b5141b;
    --red-logo:#b8262b;
    --panel-gray:#5a5a5a;
    --panel-line:#7a7a7a;
    --silver-dark:#bcbcbc;
    --silver-light:#f3f3f3;
    --text-light:#ffffff;
    --tag-gray:#555555;
    --logo-box:#e4e4e4;
  }
  *{margin:0;padding:0;box-sizing:border-box}
  html,body{width:900px;height:1200px;overflow:hidden;background:#fff}
  body{position:relative;font-family:"Caladea",Georgia,serif;color:var(--text-light)}
  .sheet{
    position:absolute;left:45px;width:768px;
    background:linear-gradient(90deg,var(--silver-dark) 0%,var(--silver-light) 45%,#dcdcdc 100%);
    background-size:256px 100%;
    box-shadow:1px 2px 4px rgba(0,0,0,.45);
    overflow:hidden;
  }
  .sheet--outside{top:27px;height:541px}
  .sheet--inside{top:610px;height:543px}
  .box{position:absolute}
  .footer-band{
    position:absolute;left:0;right:0;bottom:0;height:41px;
    background:linear-gradient(180deg,#ea3036,var(--red-deep));
    display:flex;font-size:10.5px;
  }
  .footer-band span{flex:1;text-align:center;padding-top:14px}
  .header-photo{
    left:18px;top:13px;width:735px;height:208px;
    background:linear-gradient(180deg,#7a1f8a 0%,#c21f6c 45%,#e3262d 62%,#7b0b12 75%,#d8202a 88%,#4a0710 100%);
  }
  .logo-box{background:var(--logo-box);display:flex;flex-direction:column;align-items:center;justify-content:center}
  .logo-row{display:flex;align-items:center;gap:10px}
  .logo-dot{width:34px;height:34px;border-radius:50%;background:var(--red-logo)}
  .logo-name{color:var(--red-logo);font-size:24px;line-height:24px;font-weight:400;width:150px}
  .logo-tag{color:var(--tag-gray);font-size:7px;letter-spacing:3.2px;margin-top:6px}
  .panel-gray{background:var(--panel-gray)}
  .panel-red{background:linear-gradient(180deg,var(--red),var(--red-deep))}
  .intro-copy{left:14px;top:233px;width:229px;height:248px;padding:23px 14px 0 16px;font-size:10.8px;line-height:12px}
  .intro-copy p+p{margin-top:12px}
  .hotline{left:269px;top:233px;width:229px;height:116px}
  .hotline-title{position:absolute;left:70px;top:13px;width:156px;text-align:center;font-size:12.5px;line-height:15px}
  .hotline-van{position:absolute;left:3px;top:40px;width:90px;height:64px;border-radius:8px 8px 4px 4px;background:linear-gradient(180deg,#f4f4f4,#9a9a9a)}
  .hotline-number{position:absolute;left:100px;top:75px;font-size:22px}
  .coupon{left:269px;top:363px;width:229px;height:116px;display:flex;align-items:flex-end;justify-content:center;text-align:center;font-size:10.8px;line-height:14px;padding-bottom:28px}
  .benefits{left:524px;top:233px;width:229px;height:248px;padding-top:20px}
  .benefits h2{font-weight:400;text-align:center;font-size:19px;line-height:19px}
  .benefits h3{font-weight:400;text-align:center;font-size:12.5px;line-height:14px}
  .benefit-list{list-style:none;margin:32px 14px 0 34px;font-size:10.8px;line-height:13px}
  .benefit-list li{position:relative;padding:0 0 3px 16px;margin-bottom:3px;border-bottom:1px solid var(--panel-line)}
  .benefit-list li:last-child{border-bottom:none}
  .benefit-list li::before{content:"";position:absolute;left:-1px;top:3px;width:6px;height:6px;border-radius:50%;background:#fff}
  .appreciate{left:14px;top:15px;width:229px;height:452px;text-align:center;padding:59px 18px 0;font-size:10.8px;line-height:12px}
  .appreciate h2{font-weight:400;font-size:19px;margin-bottom:32px}
  .appreciate p+p{margin-top:12px}
  .referral{left:270px;top:15px;width:229px;height:452px;text-align:center;overflow:hidden}
  .referral-photo{position:absolute;left:0;top:0;width:229px;height:200px;background:linear-gradient(160deg,rgba(255,255,255,.12),rgba(0,0,0,.08) 60%,rgba(0,0,0,0))}
  .referral h2{position:absolute;left:0;right:0;top:146px;font-weight:400;font-size:18.5px;line-height:24px}
  .referral p{position:absolute;left:24px;right:24px;font-size:10.8px;line-height:13.5px}
  .referral .ask{top:286px}
  .referral .call{top:355px}
  .treats-photo{left:512px;top:0;width:256px;height:406px;background:linear-gradient(180deg,#1d4a8c 0%,#2d7fbd 40%,#f2c6d6 62%,#6f8fb0 82%,#3d4656 100%)}
  .back-logo{left:512px;top:406px;width:256px;height:97px}
</style>
</head>
<body>

<section class="sheet sheet--outside">
  <div class="box header-photo" role="img" aria-label="City skyline at night reflected in a lake, in magenta and red tones"></div>
  <div class="box logo-box" style="left:18px;top:70px;width:250px;height:93px">
    <div class="logo-row"><span class="logo-dot"></span><span class="logo-name">Bramwell Estate Circle</span></div>
    <div class="logo-tag">Residential Sales Consultants</div>
  </div>

  <div class="box panel-gray intro-copy">
    <p>We understand that throwing a party is hard work and your budget can quickly double or even triple The same is true for home improvements and yes, even moving! That's why we have continued to grow our Client Appreciation Program.<br>We are making available an extensive inventory of items, including Moving Trucks, to make it simple on you and help you save while putting your best foot forward.</p>
    <p>We invite you to take advantage of this program when you find yourself entertaining or planning a project around the house. It comes with our complements as our way of saying THANK YOU.</p>
  </div>

  <div class="box panel-red hotline">
    <div class="hotline-title">MOVING TRUCK RESERVATION HOTLINE</div>
    <div class="hotline-van" role="img" aria-label="Front view of a white moving van"></div>
    <div class="hotline-number">123-456-789</div>
  </div>

  <div class="box panel-gray coupon">USE YOUR EXCLUSIVE COUPON CODE FOR<br>COMPLIMENTARY PARTY &amp; TOOL RENTALS AT<br>www.tpvintagehire.ex</div>

  <div class="box panel-gray benefits">
    <h2>PLATINUM LEVEL</h2>
    <h3>CLIENT BENEFITS</h3>
    <ul class="benefit-list">
      <li>FREE Use of Moving Truck</li>
      <li>FREE Premium Tool Rentals</li>
      <li>FREE Premium Concession Rentals</li>
      <li>FREE Household Rentals</li>
      <li>FREE Tool Rentals</li>
      <li>FREE Party/Event Rentals</li>
      <li>Discounted Limousine Services</li>
    </ul>
  </div>

  <div class="footer-band">
    <span>http://danfolwick.plumvesta.ex</span><span>http://danfolwick.plumvesta.ex</span><span>http://danfolwick.plumvesta.ex</span>
  </div>
</section>

<section class="sheet sheet--inside">
  <div class="box panel-gray appreciate">
    <h2>WE APPRECIATE YOU</h2>
    <p>Our business truly revolves around you. It is our first priority to ensure that each and every one of our clients receive first class service, not only during their transaction, but after as well.</p>
    <p>In an effort to show our appreciation for the trust and success that YOU, our clients, have afforded us, we have continued to grow our Client Appreciation Program to honor you. This program is designed for our most valuable assets, our most-valued Current and Past Clients.</p>
    <p>We have an extensive collection of Party, Tool, Household and Moving Items that may come in handy while entertaining friends, working around the house or making your move more affordable.<br>This program allows all of our clients to use this collection of Party, Tool, Household and Moving Items FREE OF CHARGE! This is just our way of saying Thank You for your continued Support.</p>
    <p>Sincerely,</p>
  </div>

  <div class="box panel-red referral">
    <div class="referral-photo" role="img" aria-label="Faded photo of a host serving guests at a party"></div>
    <h2>WE'D LOVE TO<br>HELP MORE<br>GREAT PEOPLE<br>LIKE YOU!</h2>
    <p class="ask">Do you know a Family Member, Friend or Professional Acquaintance who would appreciate the level of Service we provide?</p>
    <p class="call">Please call us with their name and number and we will be happy to follow-up, take great care of them and make you look REALLY good.</p>
  </div>

  <div class="box treats-photo" role="img" aria-label="Yellow and pink cotton candy on cones beside a bowl of peppermint candies"></div>
  <div class="box logo-box back-logo">
    <div class="logo-row"><span class="logo-dot"></span><span class="logo-name">Bramwell Estate Circle</span></div>
    <div class="logo-tag">Residential Sales Consultants</div>
  </div>

  <div class="footer-band">
    <span>http://danfolwick.plumvesta.ex</span><span>http://danfolwick.plumvesta.ex</span><span>http://danfolwick.plumvesta.ex</span>
  </div>
</section>

</body>
</html>
```